Simple Clean Menu for 'Crumbly Treats & Dough'!!!!

We are needing a menu for a cookie & cookie dough shop in the Philadelphia PA area called 'Crumbly' We make delicious edible cookie doughs and warm cookies.

Attached to the project is the following
1.  The menu content and pricing
2.  A competitors menu (we want it to look better than theirs!)
3.  Our logo
4. Some Images of what we serve so you better understand.
5. A hand drawn sketch we made (keep in mind we do not want a vertical menu... its just to help get your mind going)

We want the menu to be horizontal and the sections should be divided in columns from left to right not top to bottom. Column 1 - cookie dough section(with toppings at the bottom), Column 2 (or 2+3)- Gourmet cookie and signature cookie column, Column 3 (or 4) -crumblywiches and drinks

We would like custom icon designs for the dough with 1,2,3 scoops - (refer to drawings) for the cookies (not necessarily every flavor), and definitely for the crumblywiches.

The dimensions of our in store sign will be 29.75 inches h x 69.5 inches w horizontal and it will be hanging on the wall and we need all source files and infinitely scalable photoshop pdf and of course follow a lighter color scheme according to our logo etc.

Industry/Entity Type

Shop

Font styles to use
Sans Serif
Other font styles liked:
• Refer to Description + Documents

Requirements
Must have
Nice to have
Should not have

```html
<!DOCTYPE html>
<html lang="en">
<head>
<meta charset="utf-8">
<title>Crumbly Treats &amp; Dough — Menu</title>
<link rel="stylesheet" href="https://fonts.googleapis.com/css2?family=Caveat+Brush&family=Josefin+Sans:wght@400;600;700&family=Fredoka:wght@500;600&display=swap">
<style>
  :root {
    --pink: #f623c9;
    --orange: #f2a43a;
    --green: #7fe14f;
    --cyan: #74e2e6;
    --ink: #2c2c2c;
    --paper: #ffffff;
  }
  * { box-sizing: border-box; margin: 0; padding: 0; }
  html, body { width: 1200px; height: 514px; overflow: hidden; background: var(--paper); }
  .menu { position: relative; width: 1200px; height: 514px; font-family: "Josefin Sans", sans-serif; color: var(--ink); }

  .brand { position: absolute; left: 50px; top: 46px; display: flex; align-items: center; gap: 10px; }
  .brand-dot { width: 52px; height: 52px; border-radius: 50%; background: var(--orange); }
  .brand-name { font-family: "Josefin Sans", sans-serif; font-weight: 700; font-size: 46px; color: var(--ink); line-height: 1; padding-top: 8px; }

  .panel { position: absolute; border: 2px solid; border-radius: 4px; }
  .panel-title { position: absolute; top: -13px; left: 50%; transform: translateX(-50%); color: #fff; font-family: "Caveat Brush", cursive; font-size: 20px; letter-spacing: 1px; line-height: 24px; padding: 0 8px; white-space: nowrap; }
  .is-pink { border-color: var(--pink); } .is-pink .panel-title { background: var(--pink); }
  .is-orange { border-color: var(--orange); } .is-orange .panel-title { background: var(--orange); }
  .is-green { border-color: var(--green); } .is-green .panel-title { background: var(--green); }
  .is-cyan { border-color: var(--cyan); } .is-cyan .panel-title { background: var(--cyan); }

  .dough { left: 34px; top: 148px; width: 256px; height: 198px; }
  .toppings { left: 34px; top: 370px; width: 256px; height: 110px; }
  .signature { left: 307px; top: 44px; width: 282px; height: 436px; }
  .gourmet { left: 608px; top: 44px; width: 281px; height: 436px; }
  .wiches { left: 908px; top: 44px; width: 258px; height: 302px; }
  .drinks { left: 908px; top: 370px; width: 258px; height: 110px; }

  .blurb { position: absolute; font-size: 10.4px; line-height: 13.6px; }
  .dough .blurb { left: 13px; top: 28px; width: 232px; }
  .signature .blurb { left: 15px; top: 42px; width: 252px; text-align: justify; }
  .toppings .blurb { left: 10px; top: 20px; width: 236px; font-size: 10.6px; }
  .blurb b { font-weight: 700; }

  .scoops { position: absolute; left: 0; top: 116px; width: 100%; height: 48px; }
  .cone-note { position: absolute; left: 0; width: 100%; top: 176px; text-align: center; font-weight: 700; font-size: 11px; }

  .topping-art { position: absolute; left: 18px; top: 56px; width: 220px; height: 46px; border-radius: 8px; background: linear-gradient(90deg, #fbd7a3, #c8f4ae, #fff3a6, #f7bfe9); }

  .flavours { position: absolute; left: 0; width: 100%; list-style: none; text-align: center; font-family: "Josefin Sans", sans-serif; font-weight: 600; font-size: 14.5px; letter-spacing: 0.3px; }
  .flavours li { height: 34.7px; line-height: 34.7px; }
  .flavours li:nth-child(odd) { color: var(--orange); }
  .flavours li:nth-child(even) { color: var(--pink); }
  .signature .flavours { top: 133px; }
  .gourmet .flavours { top: 34px; }

  .packs { position: absolute; left: 0; top: 326px; width: 100%; height: 90px; }
  .price { font-family: "Fredoka", sans-serif; font-weight: 600; font-size: 12px; fill: var(--ink); }

  .wich { position: absolute; left: 8px; width: 244px; display: flex; gap: 6px; }
  .wich svg { flex: none; }
  .wich-name { font-family: "Josefin Sans", sans-serif; font-weight: 600; font-size: 13.5px; letter-spacing: 0.2px; }
  .wich-note { font-size: 7.4px; line-height: 9px; margin-top: 1px; }
  .wich.orange .wich-name { color: var(--orange); }
  .wich.pink .wich-name { color: var(--pink); }

  .drink { position: absolute; left: 22px; display: flex; align-items: center; gap: 14px; font-family: "Fredoka", sans-serif; font-weight: 500; font-size: 13px; }
</style>
</head>
<body>
<main class="menu">

  <div class="brand">
    <span class="brand-dot"></span>
    <span class="brand-name">Crumbly</span>
  </div>

  <section class="panel dough is-pink">
    <h2 class="panel-title">COOKIE DOUGH</h2>
    <p class="blurb">Try our many flavors of delicious edible cookie dough. Our dough tastes just like it should so you'll never know it's egg free and completely safe to eat! In a cone, in a cup, warm or cold there's no wrong way to eat our dough.</p>
    <svg class="scoops" viewBox="0 0 256 48" aria-label="Cup sizes: one scoop $4, two scoops $7, three scoops $9, cone plus $1">
      <g fill="#fff" stroke="var(--pink)" stroke-width="1.2" font-family="Josefin Sans" font-size="7" text-anchor="middle">
        <circle cx="40" cy="10" r="7"/><text x="40" y="13" fill="var(--ink)" stroke="none">1</text>
        <path d="M28 16 H52 L49 44 H31 Z" fill="var(--pink)"/>
        <text x="40" y="33" fill="#fff" stroke="none" font-weight="700">$4</text>
        <circle cx="88" cy="11" r="7"/><circle cx="101" cy="11" r="7"/>
        <text x="88" y="14" fill="var(--ink)" stroke="none">1</text><text x="101" y="14" fill="var(--ink)" stroke="none">2</text>
        <path d="M78 17 H111 L108 44 H81 Z" fill="var(--pink)"/>
        <text x="94" y="33" fill="#fff" stroke="none" font-weight="700">$7</text>
        <circle cx="160" cy="3" r="7"/><circle cx="153" cy="12" r="7"/><circle cx="167" cy="12" r="7"/>
        <text x="160" y="6" fill="var(--ink)" stroke="none">3</text><text x="153" y="15" fill="var(--ink)" stroke="none">1</text><text x="167" y="15" fill="var(--ink)" stroke="none">2</text>
        <path d="M141 18 H179 L176 44 H144 Z" fill="var(--pink)"/>
        <text x="160" y="33" fill="#fff" stroke="none" font-weight="700">$9</text>
        <text x="218" y="12" fill="var(--pink)" stroke="none" font-weight="700" font-size="9">+ $1</text>
        <path d="M206 18 H230 L218 42 Z" fill="var(--pink)" stroke="none"/>
      </g>
    </svg>
    <p class="cone-note">Eat it in a cone for $1!</p>
  </section>

  <section class="panel toppings is-green">
    <h2 class="panel-title">TOPPINGS</h2>
    <p class="blurb">Add Marshmallow, Caramel, Chocolate Syrup or Whipped Cream for <b>$0.50</b> each!</p>
    <div class="topping-art" role="img" aria-label="Row of topping illustrations: syrup bottles, whipped cream, marshmallows and a sauce splash"></div>
  </section>

  <section class="panel signature is-orange">
    <h2 class="panel-title">SIGNATURE COOKIES</h2>
    <p class="blurb">Our most decadent, gourmet cookies. 100% GMO Free, Free from Artificial colors and flavorings and made with milk, cream and butter from happy hormone free cows!</p>
    <ul class="flavours">
      <li>CHOCOLATE CHUNK</li><li>SALTED CARAMEL</li><li>LEMON BLUEBERRY</li><li>SNICKERDOODLE</li><li>PEANUT BUTTER</li>
    </ul>
    <svg class="packs" viewBox="0 0 282 90" aria-label="Single $3, six $16, twelve $30">
      <g fill="none" stroke-width="1">
        <circle cx="47" cy="28" r="9" stroke="var(--orange)"/>
        <text x="47" y="31" font-size="7" text-anchor="middle" fill="var(--ink)" stroke="none">1</text>
        <g stroke="var(--pink)"><circle cx="110" cy="20" r="8"/><circle cx="128" cy="36" r="8"/></g>
        <g stroke="var(--orange)"><circle cx="128" cy="20" r="8"/><circle cx="110" cy="36" r="8"/><circle cx="100" cy="28" r="7"/><circle cx="138" cy="28" r="7"/></g>
        <text x="119" y="31" font-size="8" text-anchor="middle" fill="var(--ink)" stroke="none">6</text>
        <g stroke="var(--pink)"><circle cx="195" cy="18" r="7"/><circle cx="225" cy="18" r="7"/><circle cx="210" cy="38" r="7"/><circle cx="240" cy="32" r="7"/><circle cx="180" cy="32" r="7"/><circle cx="255" cy="24" r="6"/></g>
        <g stroke="var(--orange)"><circle cx="210" cy="16" r="7"/><circle cx="195" cy="38" r="7"/><circle cx="225" cy="38" r="7"/><circle cx="240" cy="18" r="7"/><circle cx="180" cy="18" r="6"/><circle cx="165" cy="26" r="6"/></g>
        <text x="210" y="31" font-size="8" text-anchor="middle" fill="var(--ink)" stroke="none">12</text>
      </g>
      <text class="price" x="47" y="72" text-anchor="middle">$3</text>
      <text class="price" x="119" y="72" text-anchor="middle">$16</text>
      <text class="price" x="215" y="72" text-anchor="middle">$30</text>
    </svg>
  </section>

  <section class="panel gourmet is-pink">
    <h2 class="panel-title">GOURMET COOKIES</h2>
    <ul class="flavours">
      <li>CHOCOLATE CHIP</li><li>OATMEAL RAISIN</li><li>WHITE CHOCOLATE MACADEMIA</li><li>GLUTTEN FREE CHOCOLATE CHIP</li><li>TOFFEE CRUNCH</li><li>RED VELVET</li><li>SUGAR</li><li>CANDY BUTTON</li>
    </ul>
    <svg class="packs" viewBox="0 0 281 90" aria-label="Single $1.50, six $8, twelve $15">
      <g fill="none" stroke-width="1">
        <circle cx="47" cy="28" r="9" stroke="var(--orange)"/>
        <text x="47" y="31" font-size="7" text-anchor="middle" fill="var(--ink)" stroke="none">1</text>
        <g stroke="var(--pink)"><circle cx="121" cy="20" r="8"/><circle cx="139" cy="36" r="8"/></g>
        <g stroke="var(--orange)"><circle cx="139" cy="20" r="8"/><circle cx="121" cy="36" r="8"/><circle cx="111" cy="28" r="7"/><circle cx="149" cy="28" r="7"/></g>
        <text x="130" y="31" font-size="8" text-anchor="middle" fill="var(--ink)" stroke="none">6</text>
        <g stroke="var(--pink)"><circle cx="201" cy="18" r="7"/><circle cx="231" cy="18" r="7"/><circle cx="216" cy="38" r="7"/><circle cx="246" cy="32" r="7"/><circle cx="186" cy="32" r="7"/><circle cx="261" cy="24" r="6"/></g>
        <g stroke="var(--orange)"><circle cx="216" cy="16" r="7"/><circle cx="201" cy="38" r="7"/><circle cx="231" cy="38" r="7"/><circle cx="246" cy="18" r="7"/><circle cx="186" cy="18" r="6"/><circle cx="171" cy="26" r="6"/></g>
        <text x="216" y="31" font-size="8" text-anchor="middle" fill="var(--ink)" stroke="none">12</text>
      </g>
      <text class="price" x="47" y="72" text-anchor="middle">$1.50</text>
      <text class="price" x="130" y="72" text-anchor="middle">$ 8</text>
      <text class="price" x="216" y="72" text-anchor="middle">$15</text>
    </svg>
  </section>

  <section class="panel wiches is-orange">
    <h2 class="panel-title">CRUMBLYWICHES</h2>
    <div class="wich pink" style="top:30px">
      <svg width="32" height="24" viewBox="0 0 32 24" fill="#fff" stroke="var(--pink)" stroke-width="1.2"><ellipse cx="16" cy="18" rx="14" ry="4"/><ellipse cx="16" cy="13" rx="14" ry="4"/><ellipse cx="16" cy="8" rx="14" ry="4"/><ellipse cx="16" cy="5" rx="14" ry="4"/></svg>
      <div><p class="wich-name">THE "UN-CRUMBLYWICH" $6</p><p class="wich-note">Any flavor of our delicious cookie dough stuffed between your choice of two Gourmet Cookies!</p></div>
    </div>
    <div class="wich orange" style="top:102px">
      <svg width="32" height="24" viewBox="0 0 32 24" fill="#fff" stroke="var(--orange)" stroke-width="1.2"><path d="M3 10 A13 8 0 0 1 29 10 Z"/><path d="M3 13 Q8 11 12 13 T20 13 T29 13"/><rect x="3" y="16" width="26" height="6" rx="3"/></svg>
      <div><p class="wich-name">THE ICE CREAM CRUMBLYWICH $5</p><p class="wich-note">Creamy vanilla ice cream stuffed between your choice of any two Gourmet Cookies!</p></div>
    </div>
    <div class="wich pink" style="top:174px">
      <svg width="32" height="24" viewBox="0 0 32 24" fill="#fff" stroke="var(--pink)" stroke-width="1.2"><ellipse cx="16" cy="18" rx="14" ry="4"/><ellipse cx="16" cy="13" rx="14" ry="4"/><ellipse cx="16" cy="8" rx="14" ry="4"/><ellipse cx="16" cy="5" rx="14" ry="4"/></svg>
      <div><p class="wich-name">THE ICE CREAM DOUGHWICH $6</p><p class="wich-note">Creamy vanilla ice cream stuffed between delicious chocolate chip cookie dough…nuff said</p></div>
    </div>
    <div class="wich orange" style="top:246px">
      <svg width="32" height="24" viewBox="0 0 32 24" fill="#fff" stroke="var(--orange)" stroke-width="1.2"><path d="M3 10 A13 8 0 0 1 29 10 Z"/><path d="M3 13 Q8 11 12 13 T20 13 T29 13"/><rect x="3" y="16" width="26" height="6" rx="3"/></svg>
      <div><p class="wich-name">SIGNATURE UPGRADE: $2.50</p><p class="wich-note">Make any Crumblywich with any two Signature Cookies for just $2.50!</p></div>
    </div>
  </section>

  <section class="panel drinks is-cyan">
    <h2 class="panel-title">DRINKS</h2>
    <div class="drink" style="top:18px">
      <svg width="16" height="22" viewBox="0 0 16 22" fill="none" stroke="var(--cyan)" stroke-width="1.2"><path d="M2 2 H14 L12.5 20 H3.5 Z"/><path d="M2.6 8 H13.4"/></svg>
      <span>Water: $2.25</span>
    </div>
    <div class="drink" style="top:48px">
      <svg width="16" height="22" viewBox="0 0 16 22" fill="none" stroke="var(--pink)" stroke-width="1.2"><path d="M2 9 H12 V18 Q12 20 10 20 H4 Q2 20 2 18 Z"/><path d="M12 11 Q15 11 15 14 Q15 16 12 16"/><path d="M5 2 Q4 4 5 6 M9 2 Q8 4 9 6"/></svg>
      <span>Organic Chocolate Milk: &nbsp;$3</span>
    </div>
    <div class="drink" style="top:78px">
      <svg width="16" height="24" viewBox="0 0 16 24" fill="none" stroke="var(--orange)" stroke-width="1.2"><path d="M6 1 H10 V5 L13 9 V22 H3 V9 L6 5 Z"/><path d="M3 12 H13"/></svg>
      <span>Organic Milk: &nbsp;$3</span>
    </div>
  </section>

</main>
</body>
</html>
```